Stationary for decorative plumbing and hardware showroom
Fine Home Fittings
Professional
Wendell Okafor
2417 Morrow Parkway
Suite 420
Houston, TX 77091
wendell@lumivessa.com
www.lumivessa.com

```html
<!DOCTYPE html>
<html lang="en">
<head>
<meta charset="utf-8">
<title>LumiVessa Business Cards</title>
<link rel="stylesheet" href="https://fonts.googleapis.com/css2?family=Josefin+Sans:wght@300&family=Open+Sans:wght@400;600&display=swap">
<style>
  :root {
    --bg: #e9e6e1;
    --card: #ffffff;
    --ink: #1d1d1d;
    --band: #231f20;
    --band-text: #f2f2f2;
    --muted: #555555;
  }
  * { box-sizing: border-box; margin: 0; padding: 0; }
  html, body { width: 1200px; height: 988px; overflow: hidden; }
  body {
    background: var(--bg);
    display: flex;
    flex-direction: column;
    align-items: center;
    justify-content: center;
    gap: 48px;
    font-family: "Open Sans", sans-serif;
    color: var(--ink);
  }
  .card {
    width: 700px;
    height: 400px;
    background: var(--card);
    box-shadow: 0 10px 28px rgba(0,0,0,0.18);
    position: relative;
    overflow: hidden;
  }
  .brand { text-align: center; }
  .brand-name {
    font-family: "Josefin Sans", sans-serif;
    font-weight: 300;
    font-size: 78px;
    letter-spacing: 2px;
    color: var(--ink);
    line-height: 1;
  }
  .brand-tagline {
    font-family: "Josefin Sans", sans-serif;
    font-weight: 300;
    font-size: 17px;
    letter-spacing: 9px;
    color: var(--ink);
    margin-top: 8px;
    text-transform: uppercase;
  }
  /* back side */
  .card-back .brand { position: absolute; top: 118px; left: 0; right: 0; }
  .card-back .website {
    position: absolute;
    top: 292px;
    left: 0; right: 0;
    text-align: center;
    font-size: 16px;
    letter-spacing: 7px;
    font-style: italic;
    color: var(--muted);
  }
  /* front side */
  .card-front .brand { position: absolute; top: 38px; left: 0; right: 0; }
  .card-front .brand-name { font-size: 64px; }
  .card-front .brand-tagline { font-size: 14px; letter-spacing: 8px; }
  .contact-band {
    position: absolute;
    left: 0; right: 0; bottom: 0;
    height: 210px;
    background: var(--band);
    color: var(--band-text);
    display: flex;
    align-items: center;
  }
  .person {
    width: 350px;
    text-align: center;
    padding-left: 40px;
  }
  .person-name { font-weight: 600; font-size: 17px; margin-bottom: 34px; }
  .address { font-size: 13px; line-height: 1.55; }
  .divider { width: 1px; height: 140px; background: var(--band-text); margin: 0 20px 0 18px; }
  .contact-list { list-style: none; font-size: 13px; line-height: 1; }
  .contact-list li { display: flex; align-items: center; gap: 9px; margin: 7px 0; }
  .contact-list svg { width: 15px; height: 15px; flex: none; }
</style>
</head>
<body>
  <section class="card card-back">
    <div class="brand">
      <div class="brand-name">LumiVessa</div>
      <div class="brand-tagline">Fine Home Fittings</div>
    </div>
    <div class="website">www.LumiVessa.com</div>
  </section>

  <section class="card card-front">
    <div class="brand">
      <div class="brand-name">LumiVessa</div>
      <div class="brand-tagline">Fine Home Fittings</div>
    </div>
    <div class="contact-band">
      <div class="person">
        <div class="person-name">Wendell Okafor</div>
        <div class="address">2417 Morrow Parkway Suite 420<br>Houston, TX 77091</div>
      </div>
      <div class="divider"></div>
      <ul class="contact-list">
        <li><svg viewBox="0 0 16 16"><circle cx="8" cy="8" r="8" fill="#f2f2f2"/><path d="M5 4.5l1.6-.3.8 2-1 .8a5 5 0 0 0 2.6 2.6l.8-1 2 .8-.3 1.6c-3.5.2-6.7-3-6.5-6.5z" fill="#231f20"/></svg>713-555-0148</li>
        <li><svg viewBox="0 0 16 16"><circle cx="8" cy="8" r="8" fill="#f2f2f2"/><rect x="5.5" y="3.5" width="5" height="9" rx="1" fill="#231f20"/><rect x="6.5" y="4.8" width="3" height="5.5" fill="#f2f2f2"/></svg>832-555-0163</li>
        <li><svg viewBox="0 0 16 16"><circle cx="8" cy="8" r="8" fill="#f2f2f2"/><rect x="4" y="6.5" width="8" height="5" fill="#231f20"/><rect x="5.5" y="4" width="5" height="3" fill="#231f20"/></svg>713-555-0172</li>
        <li><svg viewBox="0 0 16 16"><circle cx="8" cy="8" r="8" fill="#f2f2f2"/><rect x="4" y="5" width="8" height="6" fill="#231f20"/><path d="M4 5l4 3.3L12 5" stroke="#f2f2f2" stroke-width="0.9" fill="none"/></svg>wendell@lumivessa.com</li>
        <li><svg viewBox="0 0 16 16"><circle cx="8" cy="8" r="8" fill="#f2f2f2"/><circle cx="8" cy="8" r="4" fill="none" stroke="#231f20" stroke-width="1"/><path d="M4 8h8M8 4c-2 2.4-2 5.6 0 8M8 4c2 2.4 2 5.6 0 8" stroke="#231f20" stroke-width="0.8" fill="none"/></svg>www.LumiVessa.com</li>
      </ul>
    </div>
  </section>
</body>
</html>
```